Local Roofing/Construction company business needs new biz card design

We need a new business card design, current cards are from the start of this operation and generic at best. We are a local Construction Company (General Contractor) with a majority of our work originating from insurance claims-exterior finish work is the main focus (Roofs-Siding-Gutters etc). Heavily involved with homeowners and the low ball offers they receive from insurance company's after a insurable event takes place. I have attached some of our original logo file(s) below.

```html
<!DOCTYPE html>
<html lang="en">
<head>
<meta charset="utf-8">
<title>Ridgeline Build Co — Business Card</title>
<link href="https://fonts.googleapis.com/css2?family=Open+Sans:wght@400;600;700&display=swap" rel="stylesheet">
<style>
  :root {
    --stage: #1c1c1f;
    --card-dark: #0b1f20;
    --card-dark-soft: #112b2a;
    --brand-green: #4fbf6e;
    --brand-green-deep: #2f9e52;
    --brand-green-light: #7fd598;
    --ink-light: #f2f5f3;
    --ink-dark: #0b1f20;
  }
  * { box-sizing: border-box; margin: 0; padding: 0; }
  html, body {
    width: 1200px; height: 780px; overflow: hidden;
    background: var(--stage);
    font-family: "Open Sans", Arial, sans-serif;
  }
  .canvas {
    width: 1200px; height: 780px;
    display: flex; align-items: center; justify-content: center; gap: 40px;
  }
  .card {
    width: 540px; height: 309px;
    border-radius: 24px;
    position: relative; overflow: hidden;
  }

  /* Back side */
  .card-back {
    background: var(--brand-green);
  }
  .back-pattern-area {
    position: absolute; inset: 0;
    background: linear-gradient(160deg, var(--brand-green-light) 0%, var(--brand-green) 45%, var(--brand-green-deep) 100%);
  }
  .back-wordmark {
    position: absolute; right: 34px; top: 118px;
    display: flex; align-items: center; gap: 8px;
    background: var(--ink-dark);
    padding: 7px 12px; border-radius: 6px;
  }
  .back-wordmark .mark-square {
    width: 14px; height: 14px; background: var(--ink-light);
  }
  .back-wordmark .wordmark-name {
    color: var(--ink-light); font-weight: 700; font-size: 14px; letter-spacing: 0.5px;
  }

  /* Front side */
  .card-front {
    background: var(--card-dark);
    border: 4px solid var(--brand-green);
  }
  .front-wordmark {
    position: absolute; left: 22px; top: 24px;
    display: flex; align-items: center; gap: 10px;
    background: var(--brand-green);
    padding: 10px 16px; border-radius: 8px;
  }
  .front-wordmark .mark-square { width: 22px; height: 22px; background: var(--ink-dark); }
  .front-wordmark .wordmark-name {
    color: var(--ink-light); font-weight: 700; font-size: 20px; letter-spacing: 0.5px;
  }
  .contact-block {
    position: absolute; left: 40px; top: 104px;
    color: var(--ink-light);
  }
  .person-name {
    color: var(--brand-green); font-weight: 700; font-size: 24px; line-height: 1.1;
  }
  .person-role { font-size: 13px; font-weight: 600; margin-top: 2px; }
  .address { font-size: 11.5px; line-height: 1.4; margin-top: 10px; }
  .contact-list { list-style: none; margin-top: 8px; font-size: 11.5px; line-height: 1.55; }
  .contact-list li { display: flex; align-items: center; gap: 7px; }
  .contact-list svg { width: 11px; height: 11px; flex: none; }

  .feature-name {
    position: absolute; right: 34px; top: 70px; text-align: right;
  }
  .feature-name .person-name { color: var(--brand-green); font-size: 22px; }
  .feature-name .person-name strong { color: var(--ink-light); font-weight: 700; }
  .feature-name .person-role { color: var(--ink-light); font-size: 12px; font-weight: 400; }
  .accent-bar {
    position: absolute; right: 0; top: 66px;
    width: 14px; height: 44px; background: var(--brand-green);
  }
</style>
</head>
<body>
<main class="canvas">
  <section class="card card-back" aria-label="Card back">
    <div class="back-pattern-area" role="img" aria-label="Repeating brand monogram pattern on green"></div>
    <div class="back-wordmark">
      <span class="mark-square"></span>
      <span class="wordmark-name">Ridgeline Build Co</span>
    </div>
  </section>

  <section class="card card-front" aria-label="Card front">
    <div class="front-wordmark">
      <span class="mark-square"></span>
      <span class="wordmark-name">Ridgeline Build Co</span>
    </div>

    <div class="contact-block">
      <p class="person-name">Mara Holloway</p>
      <p class="person-role">Co-Founder</p>
      <p class="address">42 Cedar Hollow Rd,<br>Fairbrook, MO 63011</p>
      <ul class="contact-list">
        <li>
          <svg viewBox="0 0 24 24" fill="var(--brand-green)"><path d="M6.6 10.8a15 15 0 0 0 6.6 6.6l2.2-2.2c.3-.3.7-.4 1-.2 1.1.4 2.3.6 3.6.6.6 0 1 .4 1 1V20c0 .6-.4 1-1 1A17 17 0 0 1 3 4c0-.6.4-1 1-1h3.5c.6 0 1 .4 1 1 0 1.3.2 2.5.6 3.6.1.3 0 .7-.2 1z"/></svg>
          555-210-4830
        </li>
        <li>
          <svg viewBox="0 0 24 24" fill="var(--brand-green)"><path d="M6.6 10.8a15 15 0 0 0 6.6 6.6l2.2-2.2c.3-.3.7-.4 1-.2 1.1.4 2.3.6 3.6.6.6 0 1 .4 1 1V20c0 .6-.4 1-1 1A17 17 0 0 1 3 4c0-.6.4-1 1-1h3.5c.6 0 1 .4 1 1 0 1.3.2 2.5.6 3.6.1.3 0 .7-.2 1z"/></svg>
          555-210-7719 (Emergency)
        </li>
        <li>
          <svg viewBox="0 0 24 24" fill="none" stroke="var(--brand-green)" stroke-width="2.4"><circle cx="12" cy="12" r="9"/><path d="M3 12h18M12 3c3 3.5 3 14.5 0 18M12 3c-3 3.5-3 14.5 0 18"/></svg>
          www.ridgelinebuild.com
        </li>
        <li>
          <svg viewBox="0 0 24 24" fill="none" stroke="var(--brand-green)" stroke-width="2.4"><rect x="3" y="5" width="18" height="14" rx="1"/><path d="M3 6l9 7 9-7"/></svg>
          office@ridgelinebuild.com
        </li>
      </ul>
    </div>

    <span class="accent-bar"></span>
    <div class="feature-name">
      <p class="person-name">Mara <strong>Holloway</strong></p>
      <p class="person-role">Managing Director</p>
    </div>
  </section>
</main>
</body>
</html>
```